Agriculture Business Card

I want to use my existing logo and use my tagline of "Don't Guess...Soil Test" on the card. Looking for a double sided card that will really get peoples attention.
Contact Info:
Marlow Field Crop Partners
Calvin Brusk
2716 K Lane
Otoe, NE 68592
402-555-0143
calvin.r.brusk@fieldmailbox.net

```html
<!DOCTYPE html>
<html lang="en">
<head>
<meta charset="utf-8">
<title>Marlow Field Crop Partners – Business Card</title>
<link rel="stylesheet" href="https://fonts.googleapis.com/css2?family=Oswald:wght@400;500;600&display=swap">
<style>
  :root {
    --backdrop: #d2d2d2;
    --card-white: #eeeeee;
    --ink-dark: #333333;
    --ink-mauve: #8c5e58;
    --accent-orange: #e8a020;
    --soil-brown: #7a441e;
    --soil-clay: #e08e2a;
    --leaf-green: #5aa83c;
    --tag-white: #ece8ea;
  }
  * { margin: 0; padding: 0; box-sizing: border-box; }
  html, body {
    width: 1200px; height: 1101px; overflow: hidden;
    background: var(--backdrop);
    font-family: "Oswald", sans-serif;
  }
  .canvas { position: relative; width: 1200px; height: 1101px; }

  .card { position: absolute; width: 303px; height: 534px; overflow: hidden; }
  .card-front { left: 246px; top: 266px; background: var(--card-white); text-align: center; }
  .card-back { left: 641px; top: 264px; background: var(--soil-brown); text-align: center; }

  .brand-mark {
    position: absolute; left: 50%; top: 312px; top: 46px;
    width: 72px; height: 72px; margin-left: -36px;
    border-radius: 50%; background: var(--leaf-green);
  }
  .brand-name {
    position: absolute; left: 0; right: 0; top: 150px;
    font-weight: 500; font-size: 22px; line-height: 25px;
    color: var(--ink-mauve);
  }
  .person-name {
    position: absolute; left: 0; right: 0; top: 238px;
    font-weight: 600; font-size: 42px; line-height: 48px;
    color: var(--ink-dark); letter-spacing: 0.5px;
  }
  .divider {
    position: absolute; left: 50%; width: 67px; height: 2px; margin-left: -33px;
    background: var(--accent-orange); border-radius: 1px;
  }
  .divider-top { top: 305px; }
  .divider-bottom { top: 417px; }

  .icon-row {
    position: absolute; left: 0; right: 0; top: 330px;
    display: flex; justify-content: center; gap: 8px;
  }
  .icon-row svg, .pin-icon { width: 20px; height: 20px; }
  .pin-icon { position: absolute; left: 50%; margin-left: -10px; top: 439px; }

  .contact-line {
    position: absolute; left: 0; right: 0;
    font-weight: 500; font-size: 16px; line-height: 20px; color: var(--ink-dark);
  }
  .contact-phone { top: 358px; }
  .contact-email { top: 378px; font-size: 15px; }
  .contact-address { top: 466px; }

  .tagline {
    position: absolute; left: 0; right: 0; top: 52px;
    font-weight: 500; font-size: 48px; line-height: 55px;
    color: var(--tag-white);
  }
  .back-brand {
    position: absolute; left: 0; right: 0; top: 232px;
    font-weight: 500; font-size: 20px; line-height: 24px; color: var(--tag-white);
  }
  .soil-layers {
    position: absolute; left: 0; right: 0; top: 319px; bottom: 0;
    background: linear-gradient(180deg, #b06a26 0%, var(--soil-clay) 55%, #d88a28 100%);
  }
</style>
</head>
<body>
<main class="canvas">
  <section class="card card-front" aria-label="Card front">
    <div class="brand-mark" aria-hidden="true"></div>
    <p class="brand-name">Marlow Field Crop<br>Partners</p>
    <h1 class="person-name">CALVIN BRUSK</h1>
    <div class="divider divider-top"></div>
    <div class="icon-row">
      <svg viewBox="0 0 20 20" aria-label="Phone">
        <circle cx="10" cy="10" r="10" fill="var(--ink-mauve)"/>
        <path d="M7 5.2c.6-.4 1.2-.2 1.5.4l.8 1.6c.2.5.1 1-.3 1.3l-.6.5c.5 1.2 1.4 2.2 2.6 2.8l.5-.6c.4-.4.9-.5 1.3-.3l1.6.8c.6.3.8.9.4 1.5-.6 1-1.6 1.4-2.7 1-3-1-5.3-3.5-6-6.5-.2-1.1.1-2 .9-2.5z" fill="#fff"/>
      </svg>
      <svg viewBox="0 0 20 20" aria-label="Email">
        <circle cx="10" cy="10" r="10" fill="var(--ink-mauve)"/>
        <rect x="4.8" y="6.5" width="10.4" height="7" rx="1" fill="#fff"/>
        <path d="M5.2 7l4.8 3.6L14.8 7" fill="none" stroke="var(--ink-mauve)" stroke-width="1"/>
      </svg>
    </div>
    <p class="contact-line contact-phone">402-555-0143</p>
    <p class="contact-line contact-email">calvin.r.brusk@fieldmailbox.net</p>
    <div class="divider divider-bottom"></div>
    <svg class="pin-icon" viewBox="0 0 20 20" aria-label="Address">
      <circle cx="10" cy="10" r="10" fill="var(--ink-mauve)"/>
      <path d="M10 4.5a3.6 3.6 0 0 0-3.6 3.6c0 2.7 3.6 6.6 3.6 6.6s3.6-3.9 3.6-6.6A3.6 3.6 0 0 0 10 4.5z" fill="#fff"/>
      <circle cx="10" cy="8.1" r="1.4" fill="var(--ink-mauve)"/>
    </svg>
    <p class="contact-line contact-address">2716 K Lane Otoe, NE 68592</p>
  </section>

  <section class="card card-back" aria-label="Card back">
    <h2 class="tagline">Don't Guess...<br>Soil Test</h2>
    <p class="back-brand">Marlow Field Crop Partners</p>
    <div class="soil-layers" role="img" aria-label="Stylised soil layers of rounded clay clods growing larger with depth"></div>
  </section>
</main>
</body>
</html>
```